Fresh and Modern Real Estate Land Website

This Real Estate Agent sells only land.
The wordpress design will need to work well with responsive Avada theme.
Colors should complement the attached Home-Header.jpg, the Sonoran Desert, Southwest Region of Arizona and Tucson.
Home page layout to include
- Logo Attached: NewLogo.png
- Agent Photo: MaeDorn.jpg
- Contact Detials: use Phone
- Slogan: "I Only Sell Open Land"
- Static header or Main image (see Attached Home-Header.jpg) - The dimensions of this shot may not be correct for your design. Please select from similar stock if needed and provide stock photo id.
- Intro/Welcome Text See Attached: Intro.txt
- Vertical or Horizontal display of "New" listings (include: Photo, Price, exerpt/intro) see: Properties.zip
- Tools of the trade. Home page will have a section called "Tools Of the Trade" These are items the agent uses in her work. This seciton will need to be 3 or More Images about 100 characters of text and Title. These will rotate through about 12 different tools. see: tools-of-the-trade.zip
Footer to include Contact Info/Recent Blog Posts/Testimonial
No Social Network icons
Main Menu:
Home
Properties
Testimonials
Services
About Mae
Blog
Contact
- Marck Script google/Times new Roman is logo. Designers Choice.

```html
<!DOCTYPE html>
<html lang="en">
<head>
<meta charset="utf-8">
<title>Mae Dorn – Tucson Land</title>
<link href="https://fonts.googleapis.com/css2?family=Ubuntu:wght@300;400;500;700&family=Noto+Serif:ital,wght@1,400;1,700&display=swap" rel="stylesheet">
<style>
:root{
  --orange:#f47b20;
  --orange-light:#f68a3a;
  --blue:#0f5aa0;
  --text:#333333;
  --muted:#666666;
  --footer:#23211d;
  --footer-bottom:#0b0a09;
  --white:#ffffff;
}
*{box-sizing:border-box;margin:0;padding:0}
html,body{width:832px;height:1200px;overflow:hidden;background:var(--white)}
body{position:relative;font-family:"Ubuntu",sans-serif;color:var(--text)}
.abs{position:absolute}

.brand{left:120px;top:18px;display:flex;align-items:center;gap:8px}
.brand-mark{width:14px;height:14px;border-radius:50%;background:var(--orange)}
.brand-name{font-size:30px;font-weight:500;color:var(--orange);line-height:1}

.lang{left:671px;top:6px;font-size:10px;color:#888;display:flex;align-items:center;gap:5px}
.lang-square{width:12px;height:9px;background:#3a4f8f}
.search{left:624px;top:33px;width:87px;height:17px;border:1px solid #bbb;border-radius:2px;font-size:6.5px;font-style:italic;color:#777;padding:4px 5px}
.search svg{position:absolute;right:6px;top:3px}

.nav{left:120px;top:74px;width:593px;height:28px;background:var(--orange);border-radius:4px;display:flex;justify-content:center;align-items:center;padding-left:4px}
.nav a{color:var(--white);text-decoration:none;font-size:11px;font-weight:500;padding:0 8px;border-left:1px solid rgba(255,255,255,.45);line-height:15px}
.nav a:first-child{border-left:none}

.hero{left:120px;top:110px;width:593px;height:226px;background:linear-gradient(180deg,#1c8de0 0%,#4aa8ea 38%,#b87a4f 55%,#8c7a4a 72%,#5d6b33 88%,#6e5a3a 100%)}
.hero-panel{left:0;top:37px;width:220px;height:157px;background:rgba(10,20,25,.85);padding:20px 11px}
.hero-panel h1{font-size:13px;font-weight:500;color:var(--white)}
.hero-panel p{font-size:8.5px;line-height:12.5px;color:var(--white);margin-top:8px;width:152px}
.hero-btn{position:absolute;left:11px;top:108px;width:83px;height:24px;background:linear-gradient(#f68a3a,#e8691a);border-radius:3px;color:var(--white);font-size:10.5px;line-height:24px;text-align:center}
.dots{position:absolute;left:14px;top:139px;display:flex;gap:5px}
.dots span{width:7px;height:5px;background:#888}
.dots span.on{background:var(--white)}
.hero-next{left:570px;top:98px}

.card{top:383px;width:180px}
.card-photo{width:180px;height:111px;position:relative}
.card-corner{position:absolute;left:0;top:0}
.card-head{display:flex;justify-content:space-between;margin-top:17px;font-size:13px;font-weight:500;color:var(--blue)}
.card-text{font-size:7.6px;line-height:12.5px;color:var(--muted);margin-top:13px;width:168px}
.card-foot{position:relative;height:19px;margin-top:11px;border-bottom:2px solid var(--orange-light)}
.card-btn{position:absolute;right:0;top:0;width:68px;height:16px;background:var(--orange-light);color:var(--white);font-size:7.5px;line-height:16px;text-align:center}

.welcome{left:188px;top:646px;width:456px;text-align:center}
.welcome h2{font-size:11.5px;font-weight:400;color:var(--orange)}
.welcome p{font-size:10.8px;font-weight:300;line-height:14px;color:#333;margin-top:13px}
.welcome p + p{margin-top:14px}
.welcome .hl{color:var(--orange);font-weight:400}

.box-head{height:24px;background:var(--blue);color:var(--white);font-size:11.5px;font-weight:500;padding:5px 7px;border-radius:2px}
.about{left:120px;top:824px;width:178px}
.about-body{font-size:7.8px;line-height:12.5px;color:#444;margin-top:9px;padding-left:3px}
.about-photo{float:left;width:44px;height:58px;margin:0 6px 0 0;background:linear-gradient(180deg,#b8b8b8 0%,#c98b6e 40%,#c1272d 100%)}

.tools{left:326px;top:824px;width:387px}
.tools .box-head{position:relative}
.tool-arrows{position:absolute;right:11px;top:5px;display:flex;gap:3px}
.tool{position:absolute;top:33px;width:84px;text-align:center}
.tool-photo{width:84px;height:49px}
.tool h3{font-size:7.5px;font-weight:400;color:#555;margin-top:8px}
.tool p{font-size:4.6px;line-height:8px;color:#777;margin-top:5px}
.tool-btn{display:inline-block;margin-top:7px;width:33px;height:10px;background:var(--orange-light);color:var(--white);font-size:4.5px;line-height:10px}

.footer{left:0;top:1034px;width:832px;height:139px;background:var(--footer)}
.footer-col{top:24px}
.footer-col h4{font-size:11.5px;font-weight:500;color:var(--white);width:126px;padding-bottom:4px;border-bottom:1px solid #ddd}
.contact-row{display:flex;align-items:flex-start;gap:11px;font-size:7.8px;line-height:14px;color:#ddd}
.post{display:flex;gap:6px;margin-top:10px;width:109px;padding-bottom:6px}
.post + .post{border-top:1px solid #555;padding-top:6px;margin-top:0}
.post-thumb{width:28px;height:24px;flex:none;background:linear-gradient(180deg,#9bb4c8,#8a7a5e);border:1px solid #ccc}
.post-title{font-size:5.5px;font-weight:700;color:var(--white)}
.post-text{font-size:4.6px;line-height:6.5px;color:#ddd;margin-top:2px}
.post-text b{color:var(--orange);font-weight:700}
.quote{display:flex;gap:6px;margin-top:11px;width:126px}
.quote-mark{font-family:"Noto Serif",serif;color:var(--orange);font-size:16px;line-height:12px;font-weight:700}
.quote p{font-family:"Noto Serif",serif;font-style:italic;font-size:7.2px;line-height:9px;color:#ccc;width:108px}
.quote-author{font-family:"Noto Serif",serif;font-size:7.5px;color:#ddd;margin:9px 0 0 44px}
.copyright{left:0;top:1173px;width:832px;height:27px;background:var(--footer-bottom);color:#bbb;font-size:6.8px;text-align:center;line-height:27px}
</style>
</head>
<body>

<header>
  <div class="abs brand">
    <span class="brand-mark"></span>
    <span class="brand-name">Mae Dorn</span>
  </div>
  <div class="abs lang">ENG <span class="lang-square"></span></div>
  <div class="abs search">Search site
    <svg width="10" height="10" viewBox="0 0 10 10"><circle cx="4" cy="4" r="3" fill="none" stroke="#1a5fa0" stroke-width="1.3"/><line x1="6.2" y1="6.2" x2="9.3" y2="9.3" stroke="#1a5fa0" stroke-width="1.6"/></svg>
  </div>
  <nav class="abs nav">
    <a>Home</a><a>Properties</a><a>Testimonials</a><a>Services</a><a>About Mae</a><a>Blog</a><a>Contact</a>
  </nav>
</header>

<section class="abs hero" role="img" aria-label="Desert mountain landscape with cacti under a blue sky">
  <div class="abs hero-panel">
    <h1>“I Only Sell Open Land”</h1>
    <p>Lorem ipsum dolor sit amet, conse ctetur adipisicing elit, sed do eiusm od tempor incididunt ut labore et dolore magna aliqua.</p>
    <div class="hero-btn">Learn More</div>
    <div class="dots"><span></span><span class="on"></span><span></span><span></span></div>
  </div>
  <svg class="abs hero-next" width="16" height="28" viewBox="0 0 16 28"><polyline points="2,2 14,14 2,26" fill="none" stroke="#fff" stroke-width="2"/></svg>
</section>

<section class="listings">
  <article class="abs card" style="left:120px">
    <div class="card-photo" role="img" aria-label="Desert land parcel with green brush and distant mountains" style="background:linear-gradient(180deg,#a9c6dd 0%,#8a9a80 22%,#6f8a4e 50%,#a3a58a 100%)">
      <svg class="card-corner" width="40" height="40" viewBox="0 0 40 40"><polygon points="0,0 40,0 0,40" fill="#222"/><ellipse cx="11" cy="10" rx="6" ry="4" fill="#fff"/><circle cx="11" cy="10" r="2" fill="#222"/></svg>
    </div>
    <div class="card-head"><span>Label here</span><span>$150,000</span></div>
    <p class="card-text">Lorem ipsum dolor sit amet, consectetur adipisicing elit, sed do eiusmod tempor incididunt ut labore et dolore magna aliqua.</p>
    <div class="card-foot"><span class="card-btn">Read More</span></div>
  </article>
  <article class="abs card" style="left:326px">
    <div class="card-photo" role="img" aria-label="Orange desert sunset over a dark horizon" style="background:linear-gradient(180deg,#d88a10 0%,#f1a81c 35%,#c85a0a 65%,#1c0c04 100%)">
      <svg class="card-corner" width="40" height="40" viewBox="0 0 40 40"><polygon points="0,0 40,0 0,40" fill="#222"/><ellipse cx="11" cy="10" rx="6" ry="4" fill="#fff"/><circle cx="11" cy="10" r="2" fill="#222"/></svg>
    </div>
    <div class="card-head"><span>Label here</span><span>$150,000</span></div>
    <p class="card-text">Lorem ipsum dolor sit amet, consectetur adipisicing elit, sed do eiusmod tempor incididunt ut labore et dolore magna aliqua.</p>
    <div class="card-foot"><span class="card-btn">Read More</span></div>
  </article>
  <article class="abs card" style="left:529px">
    <div class="card-photo" role="img" aria-label="Cactus-covered desert lot with mountains behind" style="background:linear-gradient(180deg,#7fa8d6 0%,#a4b3c2 28%,#7d8a5a 50%,#8e8466 100%)">
      <svg class="card-corner" width="40" height="40" viewBox="0 0 40 40"><polygon points="0,0 40,0 0,40" fill="#222"/><ellipse cx="11" cy="10" rx="6" ry="4" fill="#fff"/><circle cx="11" cy="10" r="2" fill="#222"/></svg>
    </div>
    <div class="card-head"><span>Label here</span><span>$150,000</span></div>
    <p class="card-text">Lorem ipsum dolor sit amet, consectetur adipisicing elit, sed do eiusmod tempor incididunt ut labore et dolore magna aliqua.</p>
    <div class="card-foot"><span class="card-btn">Read More</span></div>
  </article>
</section>

<section class="abs welcome">
  <h2>Welcome to the Land Desk</h2>
  <p>When you are looking for desert land, <span class="hl">Mae Dorn</span>'s focus keeps her search on open acreage across the whole valley, and that's all she sells: LAND!</p>
  <p>Mae is happy to say she works only with raw lots and acreage... yet she can point you to trusted people who handle homes. Tell her what you plan to build and where, and she will walk the parcels with you, check access and water, and help you pick the right piece of desert...for YOU!</p>
</section>

<section class="abs about">
  <div class="box-head">About Mae Dorn</div>
  <div class="about-body">
    <div class="about-photo" role="img" aria-label="Portrait of the agent"></div>
    Lorem ipsum dolor sitame con sectetur adipi sicing elit, sed do eiusmod empo incididunt ut laboret dolore magna aliqua. Ut enim ad. Deloumn dolor sit amet, consectetur adipi sicing elit, sed do eiusmod tempor incididunt ut labore et dolore magna aliqua it enim ad.
  </div>
</section>

<section class="abs tools">
  <div class="box-head">Tools of the Trade
    <div class="tool-arrows">
      <svg width="14" height="14" viewBox="0 0 14 14"><circle cx="7" cy="7" r="7" fill="#fff"/><polyline points="8.5,3.5 5,7 8.5,10.5" fill="none" stroke="#0f5aa0" stroke-width="2"/></svg>
      <svg width="14" height="14" viewBox="0 0 14 14"><circle cx="7" cy="7" r="7" fill="#fff"/><polyline points="5.5,3.5 9,7 5.5,10.5" fill="none" stroke="#0f5aa0" stroke-width="2"/></svg>
    </div>
  </div>
  <div class="tool" style="left:11px">
    <div class="tool-photo" role="img" aria-label="Yellow measuring tape" style="background:linear-gradient(180deg,#f2f2f2,#e8e2c8)"></div>
    <h3>Lorem Ipsum</h3>
    <p>Lorem ipsum dolor sit amet, consectetur adipiscing elit, sed do eiusmod tempor incididunt ut labore et dolore magna aliqua. Ut enim ad minim veniam, quis</p>
    <span class="tool-btn">Read More</span>
  </div>
  <div class="tool" style="left:142px">
    <div class="tool-photo" role="img" aria-label="Compass in a leather case" style="background:linear-gradient(180deg,#f2f2f2,#d8d6d4)"></div>
    <h3>Lorem Ipsum</h3>
    <p>Lorem ipsum dolor sit amet, consectetur adipiscing elit, sed do eiusmod tempor incididunt ut labore et dolore magna aliqua. Ut enim ad minim veniam, quis</p>
    <span class="tool-btn">Read More</span>
  </div>
  <div class="tool" style="left:274px">
    <div class="tool-photo" role="img" aria-label="Roll of orange flagging tape" style="background:linear-gradient(180deg,#f2f2f2,#f1d2c4)"></div>
    <h3>Lorem Ipsum</h3>
    <p>Lorem ipsum dolor sit amet, consectetur adipiscing elit, sed do eiusmod tempor incididunt ut labore et dolore magna aliqua. Ut enim ad minim veniam, quis</p>
    <span class="tool-btn">Read More</span>
  </div>
</section>

<footer class="abs footer">
  <div class="abs footer-col" style="left:166px">
    <h4>Contact Information</h4>
    <div class="contact-row" style="margin-top:9px">
      <svg width="12" height="12" viewBox="0 0 12 12" style="margin-top:3px"><polygon points="6,0.5 12,6 10,6 10,11.5 7.3,11.5 7.3,8 4.7,8 4.7,11.5 2,11.5 2,6 0,6" fill="#ddd"/></svg>
      <span>014 Sample Address<br>Houston, Texas 77205</span>
    </div>
    <div class="contact-row" style="margin-top:7px">
      <svg width="12" height="12" viewBox="0 0 12 12"><circle cx="6" cy="6" r="5.3" fill="none" stroke="#ddd" stroke-width="1"/><path d="M4 3.2l1 1.6-.6.7c.4.9 1 1.5 1.9 1.9l.7-.6 1.6 1-.5 1.2c-2.4-.3-4.4-2.3-4.7-4.7z" fill="#ddd"/></svg>
      <span>Phone: (012) 345-6789</span>
    </div>
    <div class="contact-row" style="margin-top:6px">
      <svg width="12" height="12" viewBox="0 0 12 12"><rect x="0.5" y="2" width="11" height="8" fill="#ddd"/><polyline points="0.5,2 6,6.5 11.5,2" fill="none" stroke="#23211d" stroke-width="1"/></svg>
      <span>maedorn@info.com</span>
    </div>
  </div>

  <div class="abs footer-col" style="left:358px">
    <h4>Recent Blog Posts</h4>
    <div class="post">
      <div class="post-thumb" role="img" aria-label="Desert land thumbnail"></div>
      <div><div class="post-title">Pollestuinim denil</div><div class="post-text">Lorem ipsum dolor sit amet, consectetur adipiscing elit, sed do eius...<b>[Read More]</b></div></div>
    </div>
    <div class="post">
      <div class="post-thumb" role="img" aria-label="Desert land thumbnail"></div>
      <div><div class="post-title">Pollestuinim denil</div><div class="post-text">Lorem ipsum dolor sit amet, consectetur adipiscing elit, sed do eius...<b>[Read More]</b></div></div>
    </div>
  </div>

  <div class="abs footer-col" style="left:540px">
    <h4>Testimonial</h4>
    <div class="quote">
      <span class="quote-mark">“</span>
      <p>Lorem ipsum dolor sit amet, consectetur adipiscing elit, sed do eiusmod tempor incid idunt ut labore et.</p>
    </div>
    <div class="quote-author">-John Doe, New York</div>
  </div>
</footer>
<div class="abs copyright">Copyright© MaeDorn2014. All Rights Reserved</div>

</body>
</html>
```